Vacation giveaway landing page design

We are giving away a holiday/vacation to Rome and we need a landing page designed that will entice people to enter their email address for a chance to win!

Full brief, examples and everything else can be found in this document: https://files.brintowle.net/papers/p/4-wxkoppTR7mnbQ2vyLazcR5xsjfPe3lhmwcKt27r/view?mode=linked

1 page

```html
<!DOCTYPE html>
<html lang="en">
<head>
<meta charset="utf-8">
<title>Win a Holiday in Rome – The Wish Weavers</title>
<link href="https://fonts.googleapis.com/css2?family=Barlow+Semi+Condensed:wght@400;500;700;800&family=Montserrat:wght@400;600&family=Open+Sans:wght@400;600&display=swap" rel="stylesheet">
<style>
:root{
  --navy:#22235a;
  --navy-deep:#1b1c48;
  --gold:#fcc200;
  --white:#ffffff;
  --ink:#111111;
  --card-text:#333333;
  --link:#1e66c9;
  --muted:#8a8a8a;
  --teal:#35c4b8;
  --sky:#a9d3f7;
}
*{box-sizing:border-box;margin:0;padding:0}
html,body{width:1200px;height:2268px;overflow:hidden}
body{font-family:"Barlow Semi Condensed",sans-serif;color:var(--white);background:var(--navy);position:relative}
.hero{position:absolute;left:0;top:0;width:1200px;height:1441px;background:var(--navy)}
.hero-photo{position:absolute;left:0;top:0;width:1200px;height:860px;
  background:linear-gradient(180deg,#1c1e3a 0%,#2a2440 20%,#4a3a3a 38%,#3a3036 52%,#2a2a4a 70%,var(--navy) 100%)}
.brand{position:absolute;top:34px;left:0;width:1200px;display:flex;justify-content:center;align-items:center;gap:12px}
.brand-mark{width:46px;height:46px;border:3px solid var(--white);border-radius:50%}
.brand-name{font-weight:800;font-size:28px;line-height:26px;letter-spacing:1px;text-transform:uppercase}
.title{position:absolute;top:160px;width:1200px;text-align:center}
.title-lead{font-weight:800;font-size:60px;line-height:62px}
.title-city{font-weight:800;font-size:104px;line-height:96px;color:var(--gold)}
.offer{position:absolute;top:345px;width:1200px;text-align:center;font-weight:500}
.offer-main{font-size:38px;line-height:46px}
.offer-sub{font-size:31px;line-height:40px;margin-top:14px;display:flex;justify-content:center;align-items:center;gap:8px}
.stars{display:flex;gap:2px}
.signup{position:absolute;top:470px;left:332px;display:flex;gap:12px}
.signup-input{width:379px;height:60px;background:#ececec;border:1px solid #ccc;font:500 21px "Barlow Semi Condensed",sans-serif;color:#333;padding:0 13px;display:flex;align-items:center}
.signup-button{width:144px;height:60px;background:var(--gold);border:0;border-radius:3px;font:800 22px "Barlow Semi Condensed",sans-serif;color:var(--ink);display:flex;align-items:center;justify-content:center}
.legal{position:absolute;top:551px;width:1200px;text-align:center;font:400 13px/24px "Open Sans",sans-serif}
.legal a{color:var(--white)}
.winners-title{position:absolute;top:702px;width:1200px;text-align:center;font-weight:800;font-size:42px}
.divider{position:absolute;top:760px;left:86px}
.card{position:absolute;top:859px;width:249px;height:473px;background:var(--white);border-radius:3px;overflow:hidden;color:var(--card-text)}
.card-photo{height:206px;background:linear-gradient(160deg,#6b6a70,#3d3434 60%,#7a5a4a)}
.card-photo.warm{background:linear-gradient(160deg,#4a2a3a,#8a6a5a 50%,#5a3040)}
.card-photo.light{background:linear-gradient(160deg,#c8c2b8,#8a7a70 50%,#d0ccc4)}
.card-head{position:absolute;top:8px;left:8px;display:flex;gap:10px;color:var(--white)}
.card-avatar{width:44px;height:44px;background:var(--white)}
.card-author{font:700 14px "Open Sans",sans-serif}
.card-time{font:400 12px "Open Sans",sans-serif;opacity:.85}
.card-body{padding:24px 12px 0 19px;font:400 13.5px/19px "Montserrat",sans-serif}
.card-body p{margin-bottom:12px}
.card-body a{color:var(--link);text-decoration:none}
.card-foot{position:absolute;bottom:0;left:15px;right:15px;height:38px;border-top:1px solid #e4e4e4;display:flex;align-items:center;gap:22px;font:600 12px "Open Sans",sans-serif;color:var(--muted)}
.arrow{position:absolute;top:1030px}
.about{position:absolute;top:1441px;left:0;width:1200px;height:517px;background:linear-gradient(180deg,#9ccaf6 0%,#b8dcf8 60%,#dff0fb 100%);color:var(--ink)}
.about-palm{position:absolute;left:0;top:100px;width:360px;height:417px;background:radial-gradient(ellipse at 40% 40%,#b7c93a,#6d9a2a 55%,rgba(150,190,80,0) 80%)}
.about-signs{position:absolute;right:0;top:0;width:225px;height:517px;background:linear-gradient(180deg,#c8783a,#d85a3a 30%,#3a8ad0 55%,#d0a050 75%,#c03050)}
.about-title{position:absolute;top:66px;left:0;width:1290px;text-align:center;font-weight:800;font-size:36px}
.about-text{position:absolute;top:128px;left:367px;width:560px;font-weight:500;font-size:18.5px;line-height:27px}
.about-text p{margin-bottom:10px}
.about-text .lead{font-weight:700}
.contact{position:absolute;top:1958px;left:0;width:1200px;height:310px;background:var(--teal);text-align:center}
.contact-title{margin-top:44px;font-weight:800;font-size:38px;line-height:46px}
.contact-email{display:inline-block;margin-top:2px;font-weight:500;font-size:23px;color:var(--white)}
.footer-links{margin-top:52px;font-weight:500;font-size:18px}
.footer-links a{color:var(--white);text-decoration:none}
.footer-legal{margin-top:14px;font-weight:500;font-size:18px;line-height:32px}
</style>
</head>
<body>
<section class="hero">
  <div class="hero-photo" role="img" aria-label="Rome at dusk: St Peter's dome above the Tiber with a lit stone bridge and reflections"></div>

  <div class="brand"><span class="brand-mark"></span><span class="brand-name">The Wish<br>Weavers</span></div>

  <h1 class="title"><div class="title-lead">WIN A HOLIDAY IN</div><div class="title-city">ROME</div></h1>

  <div class="offer">
    <div class="offer-main">4 Nights, 2 People</div>
    <div class="offer-sub">Flights + Hotel
      <span class="stars">
        <svg width="96" height="22" viewBox="0 0 96 22" fill="#fcc200">
          <g id="star"><polygon points="11,0 14,8 22,8 15.5,13 18,21 11,16 4,21 6.5,13 0,8 8,8"/></g>
          <use href="#star" x="25"/><use href="#star" x="50"/><use href="#star" x="74"/>
        </svg>
      </span>
    </div>
  </div>

  <form class="signup">
    <div class="signup-input">Enter Your Email</div>
    <div class="signup-button">SUBMIT</div>
  </form>

  <p class="legal">By entering your email, you agree to receive updates about the competition and The Wish Weavers.<br>You can review our competition <a href="#">terms and conditions here</a>.</p>

  <h2 class="winners-title">PREVIOUS WINNERS</h2>
  <svg class="divider" width="1028" height="60" viewBox="0 0 1028 60"><polyline points="0,18 478,18 514,56 550,18 1028,18" fill="none" stroke="rgba(255,255,255,.35)" stroke-width="1"/></svg>

  <svg class="arrow" style="left:86px" width="34" height="60" viewBox="0 0 34 60"><polyline points="30,2 3,30 30,58" fill="none" stroke="#c9cbe8" stroke-width="2.5"/></svg>
  <svg class="arrow" style="left:1082px" width="34" height="60" viewBox="0 0 34 60"><polyline points="4,2 31,30 4,58" fill="none" stroke="#c9cbe8" stroke-width="2.5"/></svg>

  <article class="card" style="left:160px">
    <div class="card-photo" role="img" aria-label="Winner photo in a busy city square, captioned This month's winner"></div>
    <div class="card-head"><span class="card-avatar"></span><div><div class="card-author">The Wish Weavers</div><div class="card-time">about 5 months ago</div></div></div>
    <div class="card-body">
      <p><b>Nadia Farrow</b> is the lucky winner this month!</p>
      <p>She's off to see the incredible Northern Lights in Iceland!</p>
      <p>Next month's prize? Flights to New York City! Enter to win here - <a href="#">https://wsh.example/4KpT2x</a></p>
    </div>
    <div class="card-foot"><span>▲ 12</span><span>Comment</span><span>➦ 1</span></div>
  </article>

  <article class="card" style="left:481px">
    <div class="card-photo warm" role="img" aria-label="Winner photo indoors, captioned This month's winner"></div>
    <div class="card-head"><span class="card-avatar"></span><div><div class="card-author">The Wish Weavers</div><div class="card-time">about 6 months ago</div></div></div>
    <div class="card-body">
      <p>Looks like <b>Maya</b> is the lucky one this month as she's won a trip to Valencia! What a Christmas present!</p>
      <p>Want something to look forward to in the New Year? You could win a trip to see the Northern Lights by signing up here - <a href="#">https://wsh.example/7QmL9d</a></p>
    </div>
    <div class="card-foot"><span>▲ 12</span><span>Comment</span><span>➦ 1</span></div>
  </article>

  <article class="card" style="left:792px">
    <div class="card-photo light" role="img" aria-label="Two winners celebrating in an office, captioned This month's winner"></div>
    <div class="card-head"><span class="card-avatar"></span><div><div class="card-author">The Wish Weavers</div><div class="card-time">about 7 months ago</div></div></div>
    <div class="card-body">
      <p>Congrats to this month's winner - <b>Ellie Brannock</b></p>
      <p>She was speechless when we told her that she'll be going to Rome!</p>
      <p>Next month we're giving away a trip to Valencia, get involved here for your chance to win: https://wsh.example/3VbN8k</p>
    </div>
    <div class="card-foot"><span>▲ 12</span><span>Comment</span><span>➦ 1</span></div>
  </article>
</section>

<section class="about">
  <div class="about-palm" role="img" aria-label="Palm tree fronds against the sky"></div>
  <div class="about-signs" role="img" aria-label="Colourful wooden signpost pointing to cities around the world"></div>
  <h2 class="about-title">ABOUT US</h2>
  <div class="about-text">
    <p class="lead">Holidays are too expensive, everyone knows it, but what can we do about it?</p>
    <p>My name is Tom and I started The Wish Weavers to make holidays more affordable to everybody, not just the ones with a big budget!</p>
    <p>There are some great deals out there if you know where to look, and that's what we do so that you don't have to - we spend hours searching &amp; speaking with companies to find you the best deals the world of travel has to offer.</p>
    <p>So if you wish you could get away more often &amp; you like the idea of flights to <b>Toronto for just £199</b>, New York for £233, or booking a <b>hotel for 70% off,</b> then enter your email above!</p>
  </div>
</section>

<footer class="contact">
  <h2 class="contact-title">CONTACT</h2>
  <a class="contact-email" href="#">hello@thewishweavers.example</a>
  <div class="footer-links"><a href="#">Terms &amp; Conditions</a> &nbsp;|&nbsp; <a href="#">Privacy Policy</a></div>
  <div class="footer-legal">© 2018 Vellmore Holdings LTD a private limited company registered in England and Wales, Reg No: 10482217.<br>Reg office and postal address: 42 Harbour Lane, London, E14 2QX, UK</div>
</footer>
</body>
</html>
```